Bluewake Skipper Services LLC

I'd like business cards with a logo and words to describe my services and qualifications. I want to emphasize the wide variety of services offered and my professional qualifications. Words to include "Bluewake Skipper Services LLC", "Motor and Sailing Vessel Delivery, Charter, Surveys, Towing and Instruction". Qualifications I would like to include are "Captain Rob Dellaway, NMLB Master Mariner, 200 ton, Ocean". Include address, phone and email: "48215 Hollowmere Lane, Fairfax Station, VA 20417, (C) 703-492-6078, BluewakeSkipperServices@postvelo.net"

Target Market(s)

I am targeting recreational boaters and commercial customers that need people to operate their boats for charter or delivery to another location.

Industry/Entity Type

boat selling/buying, boat charter, boat recreation

Logo Text

"Motor and Sailing Vessel Delivery, Charters, Surveys, Towing and Instruction"

Requirements
Must have
• A professional and nautical look.
Nice to have
• May be nice to have a muted chart as the background design
Should not have
• colors or design that obscure the message of offering a wide range of professional boat captain services

```html
<!DOCTYPE html>
<html lang="en">
<head>
<meta charset="utf-8">
<title>Bluewake Skipper Services LLC – Business Card</title>
<link rel="stylesheet" href="https://fonts.googleapis.com/css2?family=Montserrat:wght@400;500;600;700;800&display=swap">
<style>
  :root {
    --canvas-bg: #eef0f3;
    --chart-deep: #a7b5cb;
    --chart-mid: #c3cedd;
    --chart-light: #e2e8f0;
    --panel: #ffffff;
    --navy: #2b3858;
    --text: #2f3a52;
    --accent: #4aa8e8;
  }
  * { margin: 0; padding: 0; box-sizing: border-box; }
  html, body {
    width: 1200px;
    height: 900px;
    overflow: hidden;
    background: var(--canvas-bg);
    font-family: "Montserrat", Arial, sans-serif;
  }
  .business-card {
    position: absolute;
    left: 75px;
    top: 150px;
    width: 1050px;
    height: 600px;
    overflow: hidden;
    box-shadow: 0 6px 24px rgba(40, 55, 85, 0.18);
  }
  .chart-background {
    position: absolute;
    inset: 0;
    background: linear-gradient(120deg, var(--chart-deep) 0%, var(--chart-mid) 45%, var(--chart-light) 75%, var(--chart-mid) 100%);
  }
  .panel {
    position: absolute;
    background: var(--panel);
    color: var(--text);
  }
  .brand-panel {
    left: 44px;
    top: 110px;
    width: 464px;
    height: 350px;
    display: flex;
    flex-direction: column;
    align-items: center;
    text-align: center;
    padding-top: 36px;
  }
  .brand-mark {
    width: 96px;
    height: 96px;
  }
  .brand-name {
    margin-top: 18px;
    color: var(--navy);
    font-weight: 700;
    line-height: 1;
  }
  .brand-name-main {
    display: block;
    font-size: 50px;
    letter-spacing: -1px;
  }
  .brand-name-sub {
    display: block;
    margin-top: 8px;
    font-size: 14px;
    letter-spacing: 6px;
    text-transform: uppercase;
  }
  .services {
    margin-top: 36px;
    width: 360px;
    font-size: 17px;
    line-height: 1.3;
    font-weight: 400;
  }
  .captain-panel {
    left: 745px;
    top: 7px;
    width: 290px;
    height: 120px;
    padding: 20px 0 0 24px;
    line-height: 1.25;
  }
  .captain-name {
    font-size: 22px;
    font-weight: 700;
    color: var(--navy);
  }
  .credential {
    font-size: 19px;
    font-weight: 400;
    padding-left: 8px;
  }
  .contact-panel {
    left: 558px;
    top: 453px;
    width: 492px;
    height: 127px;
    padding: 14px 22px 0 0;
    text-align: right;
    font-size: 19px;
    line-height: 1.3;
  }
</style>
</head>
<body>
  <article class="business-card">
    <div class="chart-background" role="img" aria-label="Muted nautical world chart with grid lines and ocean labels"></div>

    <section class="panel brand-panel">
      <svg class="brand-mark" viewBox="0 0 96 96" aria-hidden="true">
        <circle cx="48" cy="48" r="40" fill="var(--accent)"/>
      </svg>
      <h1 class="brand-name">
        <span class="brand-name-main">Bluewake</span>
        <span class="brand-name-sub">Skipper Services LLC</span>
      </h1>
      <p class="services">Motor and Sailing Vessel Delivery, Charter, Surveys, Towing and Instruction</p>
    </section>

    <section class="panel captain-panel">
      <p class="captain-name">Captain Rob Dellaway</p>
      <p class="credential">NMLB Master Mariner</p>
      <p class="credential">&nbsp;200 ton, Ocean</p>
    </section>

    <section class="panel contact-panel">
      <p>48215 Hollowmere Lane</p>
      <p>Fairfax Station, VA 20417</p>
      <p>(C) 703-492-6078</p>
      <p>BluewakeSkipperServices@postvelo.net</p>
    </section>
  </article>
</body>
</html>
```